Business Card Design

BrightHarbor is a fund management company that takes just four market positions a year. each position is linked to a big geopolitical and economic event happening in the world. So for example we may be buying gold mining stocks-these are the companies who dig the gold out of the ground, as all the gold is currently being bought by Asia, or buying the japanese stock market as this is one of the big stories of today.

I am looking for a logo that represents 'BrightHarbor'-the Bright Harbor.

I would like it to be small and sit to the left of the name of the company on the left hand side(I think!)on the top line of the business card please.

Industry/Entity Type

Mining

Contact Information for Business Card

BrightHarbor Capital management Ltd
41 Pellam Street
London E9T 2QN

Martin J Colby

Mob: 0(44)7823946250
Off: 0(44) 207 xxxx
email: mc@brightharbor-cm.example

```html
<!DOCTYPE html>
<html lang="en">
<head>
<meta charset="utf-8">
<title>BrightHarbor Capital management Ltd – Business Card</title>
<link rel="stylesheet" href="https://fonts.googleapis.com/css2?family=Arimo:wght@400;700&display=swap">
<style>
  :root {
    --card-bg: #ffffff;
    --ink: #000000;
    --mark-blue: #3a9be8;
  }
  html, body {
    margin: 0;
    padding: 0;
    width: 1200px;
    height: 702px;
    overflow: hidden;
    background: var(--card-bg);
  }
  .card {
    position: relative;
    width: 1200px;
    height: 702px;
    background: var(--card-bg);
    color: var(--ink);
    font-family: "Arimo", Arial, sans-serif;
  }
  .brand-mark {
    position: absolute;
    left: 156px;
    top: 97px;
    width: 110px;
    height: 110px;
  }
  .company {
    position: absolute;
    left: 286px;
    top: 126px;
    margin: 0;
    white-space: nowrap;
    line-height: 1;
    font-weight: 400;
  }
  .company-name {
    font-size: 44px;
  }
  .company-suffix {
    font-size: 35px;
  }
  .person-name {
    position: absolute;
    left: 0;
    width: 1218px;
    top: 210px;
    margin: 0;
    text-align: center;
    font-size: 40px;
    font-weight: 700;
    line-height: 1;
  }
  .contact-line {
    position: absolute;
    left: 98px;
    margin: 0;
    font-size: 30px;
    line-height: 1;
    white-space: nowrap;
  }
  .contact-mobile { top: 372px; }
  .contact-office { top: 411px; }
  .contact-email  { top: 449px; }
  .address-street { top: 495px; }
  .address-city   { top: 534px; }
  .address-post   { top: 573px; }
</style>
</head>
<body>
  <main class="card">
    <svg class="brand-mark" viewBox="0 0 110 110" aria-hidden="true">
      <circle cx="55" cy="55" r="55" fill="var(--mark-blue)"/>
    </svg>
    <h1 class="company">
      <span class="company-name">BrightHarbor</span>
      <span class="company-suffix">Capital management Ltd</span>
    </h1>
    <h2 class="person-name">Martin J Colby</h2>
    <p class="contact-line contact-mobile">Mob: 0(44)7823946250</p>
    <p class="contact-line contact-office">Off: 0(44) 207 xxxx</p>
    <p class="contact-line contact-email">email: mc@brightharbor-cm.example</p>
    <p class="contact-line address-street">41 Pellam Street</p>
    <p class="contact-line address-city">London</p>
    <p class="contact-line address-post">E9T 2QN</p>
  </main>
</body>
</html>
```